business card for a massage therapy practice named 'Meadow and Rowan Massage Studio'

I really need a trendy, yet easy on the eyes business card to complement my logo. Ideally with some gold or rose gold foil work.

My uploaded file of the logo I have in horizontal but I have a vertical version as well. Another color that is used in the website is a blush pink here and there. I'd like to see some trendy tropical leaves in the design.

```html
<!DOCTYPE html>
<html lang="en">
<head>
<meta charset="UTF-8">
<title>Meadow and Rowan Massage Studio – Business Card</title>
<link rel="stylesheet" href="https://fonts.googleapis.com/css2?family=Oswald:wght@600&family=Work+Sans:wght@400;500&display=swap">
<style>
  :root {
    --backdrop: #262627;
    --card: #141414;
    --card-edge: #1d1d1d;
    --foil: #d4d4d4;
    --foil-soft: #a9a9a9;
    --spot-gloss: #3b3b3b;
    --divider: #6a6a6a;
  }
  * { margin: 0; padding: 0; box-sizing: border-box; }
  html, body {
    width: 1200px; height: 900px; overflow: hidden;
    background: var(--backdrop);
  }
  .sheet {
    position: relative; width: 1200px; height: 900px;
    display: flex; flex-direction: column; align-items: center; justify-content: center;
    gap: 28px;
  }
  .card {
    position: relative; width: 700px; height: 400px;
    background: linear-gradient(160deg, var(--card-edge), var(--card) 60%);
    box-shadow: 0 8px 24px rgba(0,0,0,.45);
  }
  /* front */
  .card-front { display: flex; align-items: center; justify-content: center; }
  .brand-name {
    font-family: "Work Sans", sans-serif; font-weight: 500;
    color: var(--foil); text-align: center;
    font-size: 40px; line-height: 1.25; letter-spacing: 1px;
  }
  .brand-name span { display: block; font-size: 22px; letter-spacing: 6px; text-transform: uppercase; }
  /* back */
  .card-back { padding: 0 56px; }
  .holder-name {
    position: absolute; left: 56px; top: 150px;
    font-family: "Oswald", sans-serif; font-weight: 600;
    font-size: 40px; letter-spacing: 2px; text-transform: uppercase;
    color: var(--spot-gloss);
  }
  .divider {
    position: absolute; left: 368px; top: 140px; width: 1px; height: 70px;
    background: var(--divider);
  }
  .contact-list {
    position: absolute; left: 396px; top: 140px; list-style: none;
    font-family: "Work Sans", sans-serif; font-size: 17px; color: var(--foil);
    line-height: 24px;
  }
  .contact-list li { display: flex; align-items: center; gap: 10px; }
  .contact-list svg { width: 12px; height: 12px; flex: none; }
  .address {
    position: absolute; left: 80px; bottom: 80px;
    font-family: "Work Sans", sans-serif; font-size: 17px; color: var(--spot-gloss);
  }
</style>
</head>
<body>
<main class="sheet">
  <section class="card card-front">
    <h1 class="brand-name">Meadow &amp; Rowan <span>Massage Studio</span></h1>
  </section>

  <section class="card card-back">
    <h2 class="holder-name">Dana Whitfield</h2>
    <div class="divider"></div>
    <ul class="contact-list">
      <li>
        <svg viewBox="0 0 12 12" aria-hidden="true"><path d="M2.5 1h2l1 3-1.3 1a6 6 0 0 0 2.8 2.8l1-1.3 3 1v2a1 1 0 0 1-1 1A9.5 9.5 0 0 1 1.5 2a1 1 0 0 1 1-1z" fill="var(--foil-soft)"/></svg>
        (555) 214-0387
      </li>
      <li>
        <svg viewBox="0 0 12 12" aria-hidden="true"><rect x="1" y="2.5" width="10" height="7" fill="none" stroke="var(--foil-soft)" stroke-width="1.2"/><path d="M1 2.5l5 4 5-4" fill="none" stroke="var(--foil-soft)" stroke-width="1.2"/></svg>
        meadowandrowan@mail.com
      </li>
      <li>
        <svg viewBox="0 0 12 12" aria-hidden="true"><circle cx="6" cy="6" r="5" fill="none" stroke="var(--foil-soft)" stroke-width="1.2"/><ellipse cx="6" cy="6" rx="2.2" ry="5" fill="none" stroke="var(--foil-soft)" stroke-width="1"/><path d="M1 6h10" stroke="var(--foil-soft)" stroke-width="1"/></svg>
        www.meadowandrowan.com
      </li>
    </ul>
    <p class="address">240 Linden Ave. suite 12, Fairview, CA 90210</p>
  </section>
</main>
</body>
</html>
```